Payday Lending App Interface Design

Hello, we are building a payday lending application, Lendoro, that lend people money. I have drafted some of the screens that show the functionalities we have at the moment, please find the screens in attachments.
The elements in the screens are placed just to show what should be included in those screens, it's not necessary to follow the same layout. If you have better design ideas, you are very welcomed to show off your talent.
I think what we want is a style guide so that we can apply the same style to any screens that are similar to the ones I attached. We really like
the style as in the attached image called Style.png. We might want something similar - a simple, clean design yet fun and engaging. Customised graphical elements such as icons, illustrations are preferable.
Apart from the attached screens, we might also need a design for the On Board screen and the Login/Sign Up screen too.
Our logo colour is in yellow and black. Perhaps we will have a similar colour theme. I also attached the logo file, icon-Lendoro.png, if you would like to put it in your design.
Please message me if you need further information.
Regards
Target Market(s)
Young people that doesn't have strong income
Look and feel
Each slider illustrates characteristics of the customer's brand and the style your logo design should communicate.

```html
<!DOCTYPE html>
<html lang="en">
<head>
<meta charset="utf-8">
<title>Lendoro – Homescreen &amp; Loan Summary</title>
<link href="https://fonts.googleapis.com/css2?family=Poppins:wght@400;500;600;700&display=swap" rel="stylesheet">
<style>
  :root{
    --ink:#0d0d0f;
    --navy:#1f242c;
    --text:#3b3b3b;
    --muted:#9a9a9a;
    --yellow:#ffc200;
    --red:#e52626;
    --green:#3aa84a;
    --grey:#9d9d9d;
    --tile:#f4f4f4;
    --card:#ffffff;
    --white:#ffffff;
  }
  *{box-sizing:border-box;margin:0;padding:0}
  html,body{width:830px;height:1200px;overflow:hidden;background:var(--white)}
  body{font-family:"Poppins",sans-serif;color:var(--ink);position:relative}

  .section-head{position:absolute;top:20px}
  .section-head h1{font-size:26px;font-weight:700;line-height:1.2}
  .section-head h2{font-size:14px;font-weight:700;margin-top:14px}
  .section-head li{font-size:14px;font-weight:400;margin-left:24px;color:#1d2333;line-height:1.4}
  .head-home{left:51px}
  .head-summary{left:437px}

  .phone{position:absolute;border:3px solid var(--ink);border-radius:31px;background:var(--white);overflow:hidden}
  .phone-home{left:49px;top:135px;width:337px;height:851px}
  .phone-summary{left:435px;top:135px;width:356px;height:1038px}

  .status{position:absolute;top:14px;left:0;right:0;height:18px;display:flex;justify-content:space-between;align-items:center;padding:0 14px 0 28px;font-size:13px;font-weight:600}
  .phone-summary .status{padding-left:31px;padding-right:22px}

  /* home header */
  .home-header{position:absolute;left:0;top:0;width:100%;height:184px;background:linear-gradient(160deg,#121418,#2a2f38);border-radius:0 0 26px 26px;color:var(--white);overflow:hidden}
  .home-header .status{color:var(--white)}
  .landscape{position:absolute;left:0;bottom:0;width:100%;height:95px;background:linear-gradient(180deg,rgba(60,66,76,0) 0%,rgba(56,62,72,.55) 60%,rgba(44,49,58,.7) 100%);border-radius:0 0 26px 26px}
  .nav-bar{position:absolute;top:54px;left:20px;right:18px;display:flex;align-items:center;justify-content:space-between}
  .nav-title{font-size:21px;font-weight:600;position:absolute;left:50%;transform:translateX(-50%)}
  .nav-actions{display:flex;gap:8px;align-items:center}
  .greeting{position:absolute;left:34px;top:113px;font-size:16px;line-height:24px}
  .greeting strong{font-weight:700;display:block}

  /* steps */
  .timeline{position:absolute;left:38px;top:260px;height:515px;border-left:2px dashed #555}
  .dot{position:absolute;left:24px;width:30px;height:30px;border-radius:50%;display:flex;align-items:center;justify-content:center}
  .dot.done{background:var(--green)}
  .dot.error{background:var(--red)}
  .dot.pending{background:var(--yellow)}
  .dot.locked{background:var(--grey)}
  .step{position:absolute;left:73px;width:240px;background:var(--card);border-radius:14px;box-shadow:0 2px 12px rgba(0,0,0,.06);padding:12px 18px}
  .step h3{font-size:14.5px;font-weight:600;line-height:1.5}
  .step p{font-size:12.5px;line-height:19px;color:var(--text);margin-top:3px}
  .step.error h3{color:var(--red)}
  .step.pending h3{color:var(--yellow)}
  .step.locked h3{color:var(--muted)}
  .step.locked p{color:#aaa}

  /* summary */
  .back{position:absolute;left:24px;top:62px}
  .summary-title{position:absolute;left:0;right:0;top:54px;text-align:center;font-size:21px;font-weight:600}
  .notice{position:absolute;left:25px;top:110px;width:306px;height:67px;background:var(--ink);border-radius:8px;color:var(--white);display:flex;align-items:center;padding:0 14px 0 18px;gap:12px}
  .notice p{font-size:11px;line-height:16px}
  .notice em{font-style:normal;color:var(--yellow)}
  .info-row{position:absolute;left:25px;width:306px;height:75px;background:var(--tile);border-radius:14px;display:flex;align-items:center;padding-left:14px;gap:14px}
  .info-icon{width:52px;height:52px;border-radius:12px;background:#ececec;display:flex;align-items:center;justify-content:center}
  .info-row h4{font-size:15.5px;font-weight:600;line-height:1.4}
  .info-row span{font-size:13.5px;color:var(--text)}
  .agreement{position:absolute;left:25px;top:596px;width:306px;height:306px;background:var(--card);border-radius:10px;box-shadow:0 2px 12px rgba(0,0,0,.05);padding:14px 14px 0}
  .agreement h4{font-size:13px;font-weight:600;margin-bottom:2px}
  .agreement h5{font-size:11.5px;font-weight:600;color:var(--text);line-height:17px}
  .agreement p{font-size:11.5px;line-height:17px;color:var(--text);text-align:justify}
  .cta{position:absolute;left:25px;top:928px;width:306px;height:56px;background:var(--yellow);border-radius:15px;display:flex;align-items:center;justify-content:center;font-size:13.5px;font-weight:600;color:var(--ink)}
</style>
</head>
<body>

<header class="section-head head-home">
  <h1>Homescreen</h1>
  <h2>Revised</h2>
  <ul><li>Added simple landscape vector</li></ul>
</header>

<header class="section-head head-summary">
  <h1>Loan Summary</h1>
  <h2>Revised</h2>
  <ul><li>Added some highlighted section space</li></ul>
</header>

<!-- Homescreen -->
<section class="phone phone-home">
  <div class="home-header">
    <div class="landscape" role="img" aria-label="Soft dark landscape of rolling hills with a moon"></div>
    <div class="status">
      <span>9:41</span>
      <svg width="60" height="12" viewBox="0 0 60 12" fill="#fff">
        <rect x="0" y="8" width="2.5" height="4" rx=".5"/><rect x="4" y="6" width="2.5" height="6" rx=".5"/><rect x="8" y="3.5" width="2.5" height="8.5" rx=".5"/><rect x="12" y="1" width="2.5" height="11" rx=".5"/>
        <path d="M26 11.5l-2-2a3 3 0 014 0zM22.5 8a5 5 0 017 0l1.2-1.2a6.8 6.8 0 00-9.4 0zM20 5.5a8.5 8.5 0 0112 0l1.2-1.2a10.2 10.2 0 00-14.4 0z"/>
        <rect x="38" y="1.5" width="19" height="9" rx="2.5" fill="none" stroke="#fff" stroke-opacity=".5"/><rect x="39.5" y="3" width="16" height="6" rx="1.5"/><rect x="58" y="4.5" width="1.3" height="3" rx=".5" fill-opacity=".5"/>
      </svg>
    </div>
    <div class="nav-bar">
      <svg width="27" height="22" viewBox="0 0 27 22" fill="#fff"><rect y="1" width="27" height="3" rx="1.5"/><rect y="9.5" width="27" height="3" rx="1.5"/><rect y="18" width="27" height="3" rx="1.5"/></svg>
      <span class="nav-title">Welcome</span>
      <div class="nav-actions">
        <svg width="26" height="26" viewBox="0 0 26 26">
          <path d="M12 3a6 6 0 00-6 6v5l-2.5 4h17L18 14V9a6 6 0 00-6-6z" fill="#fff"/><path d="M9.5 20a2.5 2.5 0 005 0z" fill="#fff"/>
          <circle cx="18.5" cy="6" r="5" fill="var(--yellow)"/>
        </svg>
        <svg width="27" height="27" viewBox="0 0 24 24" fill="none" stroke="#fff" stroke-width="1.7" stroke-linejoin="round">
          <path d="M10.3 2h3.4l.5 2.6 1.9.8 2.2-1.5 2.4 2.4-1.5 2.2.8 1.9 2.6.5v3.4l-2.6.5-.8 1.9 1.5 2.2-2.4 2.4-2.2-1.5-1.9.8-.5 2.6h-3.4l-.5-2.6-1.9-.8-2.2 1.5-2.4-2.4 1.5-2.2-.8-1.9L2 13.7v-3.4l2.6-.5.8-1.9-1.5-2.2 2.4-2.4 2.2 1.5 1.9-.8z"/>
          <circle cx="12" cy="12" r="3.3"/>
        </svg>
      </div>
    </div>
    <p class="greeting">Hello,<strong>Jordan Reeve</strong></p>
  </div>

  <div class="timeline"></div>

  <span class="dot done" style="top:245px"><svg width="16" height="16" viewBox="0 0 16 16"><path d="M2.5 8.5l3.5 3.5 7.5-8" fill="none" stroke="#fff" stroke-width="2.6" stroke-linecap="round" stroke-linejoin="round"/></svg></span>
  <span class="dot error" style="top:362px"><svg width="14" height="14" viewBox="0 0 14 14"><path d="M3 3l8 8M11 3l-8 8" stroke="#fff" stroke-width="2.6" stroke-linecap="round"/></svg></span>
  <span class="dot done" style="top:469px"><svg width="16" height="16" viewBox="0 0 16 16"><path d="M2.5 8.5l3.5 3.5 7.5-8" fill="none" stroke="#fff" stroke-width="2.6" stroke-linecap="round" stroke-linejoin="round"/></svg></span>
  <span class="dot pending" style="top:558px"><svg width="6" height="18" viewBox="0 0 6 18"><rect x="1.5" y="0" width="3" height="11" rx="1.5" fill="#fff"/><circle cx="3" cy="15.5" r="1.8" fill="#fff"/></svg></span>
  <span class="dot locked" style="top:660px"></span>
  <span class="dot locked" style="top:760px"></span>

  <article class="step" style="top:216px;height:87px">
    <h3>Get Started</h3>
    <p>What you need to know before applying a loan</p>
  </article>
  <article class="step error" style="top:327px;height:102px">
    <h3>Basic Information</h3>
    <p>Your ID document are expired. Upload your document again to get qualified</p>
  </article>
  <article class="step" style="top:453px;height:61px">
    <h3>Connect Bank Account</h3>
    <p>Add your own bank account</p>
  </article>
  <article class="step pending" style="top:538px;height:70px">
    <h3>Apply a Loan</h3>
    <p>Get a loan that fit to your needs</p>
  </article>
  <article class="step locked" style="top:633px;height:87px">
    <h3>Repayments</h3>
    <p>Pay your installments before due date!</p>
  </article>
  <article class="step locked" style="top:743px;height:66px">
    <h3>Loan Closed</h3>
    <p>Thank you for using Lendoro</p>
  </article>
</section>

<!-- Loan Summary -->
<section class="phone phone-summary">
  <div class="status">
    <span>9:41</span>
    <svg width="62" height="12" viewBox="0 0 62 12" fill="#000">
      <rect x="0" y="8" width="2.5" height="4" rx=".5"/><rect x="4" y="6" width="2.5" height="6" rx=".5"/><rect x="8" y="3.5" width="2.5" height="8.5" rx=".5"/><rect x="12" y="1" width="2.5" height="11" rx=".5"/>
      <path d="M26 11.5l-2-2a3 3 0 014 0zM22.5 8a5 5 0 017 0l1.2-1.2a6.8 6.8 0 00-9.4 0zM20 5.5a8.5 8.5 0 0112 0l1.2-1.2a10.2 10.2 0 00-14.4 0z"/>
      <rect x="39" y="1.5" width="20" height="9" rx="2.5" fill="none" stroke="#000" stroke-opacity=".4"/><rect x="40.5" y="3" width="17" height="6" rx="1.5"/><rect x="60" y="4.5" width="1.3" height="3" rx=".5" fill-opacity=".4"/>
    </svg>
  </div>

  <svg class="back" width="12" height="20" viewBox="0 0 12 20"><path d="M10 2L3 10l7 8" fill="none" stroke="#000" stroke-width="2.8" stroke-linecap="round" stroke-linejoin="round"/></svg>
  <h2 class="summary-title">Loan Summary</h2>

  <div class="notice">
    <svg width="19" height="19" viewBox="0 0 20 20" style="flex:none"><circle cx="10" cy="10" r="10" fill="#fff"/><rect x="8.7" y="8.5" width="2.6" height="7" rx="1" fill="#000"/><circle cx="10" cy="5.6" r="1.5" fill="#000"/></svg>
    <p>The following schedule (your "<em>Loan Repayment Schedule</em>") sets out the details of your loan and your repayment obligations</p>
  </div>

  <div class="info-row" style="top:202px">
    <span class="info-icon"><svg width="26" height="28" viewBox="0 0 26 28"><circle cx="13" cy="7.5" r="6.5"/><path d="M1 27v-3a8 8 0 018-8h8a8 8 0 018 8v3z"/></svg></span>
    <div><h4>Application Name</h4><span>Jordan Reeve</span></div>
  </div>
  <div class="info-row" style="top:302px">
    <span class="info-icon"><svg width="26" height="28" viewBox="0 0 26 28"><path d="M8 1h10l-3 5h-4z"/><path d="M10 7h6c6 3 9 8 9 13 0 5-4 7-12 7S1 25 1 20c0-5 3-10 9-13z"/><text x="13" y="23" font-family="Poppins,sans-serif" font-size="13" font-weight="700" fill="#fff" text-anchor="middle">$</text></svg></span>
    <div><h4>Amount Borrowed</h4><span>$ 2,500</span></div>
  </div>
  <div class="info-row" style="top:402px">
    <span class="info-icon"><svg width="26" height="26" viewBox="0 0 26 26"><rect x="6" y="1" width="3" height="5" rx="1"/><rect x="17" y="1" width="3" height="5" rx="1"/><path d="M1 7a3 3 0 013-3h18a3 3 0 013 3v3H1z"/><path d="M1 12h24v11a3 3 0 01-3 3H4a3 3 0 01-3-3z"/><rect x="18" y="7" width="4" height="2" fill="#ececec"/></svg></span>
    <div><h4>Repayment Cycle</h4><span>Fortnightly</span></div>
  </div>
  <div class="info-row" style="top:502px">
    <span class="info-icon"><svg width="22" height="28" viewBox="0 0 22 28"><path d="M2 1h12l7 7v18a1 1 0 01-1 1H2a1 1 0 01-1-1V2a1 1 0 011-1z" fill="none" stroke="#000" stroke-width="2"/><path d="M14 1v7h7" fill="none" stroke="#000" stroke-width="2"/><text x="7" y="14" font-family="Poppins,sans-serif" font-size="11" font-weight="700" text-anchor="middle">$</text><rect x="5" y="17" width="12" height="2"/><rect x="5" y="21" width="12" height="2"/><rect x="12" y="9" width="5" height="2"/><rect x="12" y="13" width="5" height="2"/></svg></span>
    <div><h4>Loan Term</h4><span>6 Months</span></div>
  </div>

  <article class="agreement">
    <h4>Loan Agreement</h4>
    <h5>Lorem Ipsum</h5>
    <p>Lorem ipsum dolor sit amet, consectetur adipiscing elit, sed do eiusmod tempor incididunt ut labore et dolore magna aliqua. Integer enim neque volutpat ac. Mi quis hendrerit dolor magna eget est lorem ipsum dolor. Aenean vel elit scelerisque mauris pellentesque pulvinar pellentesque habitant.</p>
    <h5>Lorem Ipsum</h5>
    <p>Massa tincidunt dui ut ornare lectus sit amet est. Et egestas quis ipsum suspendisse ultrices gravida dictum fusce ut. Pulvinar neque laoreet suspendisse interdum consectetur. Sodales ut etiam sit amet nisl purus. Dui faucibus in ornare quam.</p>
  </article>

  <div class="cta">Confirm and Agree</div>
</section>

</body>
</html>
```